creative pack design with extended budget for Velmoraq coffee product

- we need a packing design for a new product of coffee for our company Tesmo Kirul located in Uganda.
- specialty Arabica coffee grown at slopes of Mountain Elgon with rich volcanic soils located in Eastern region of Uganda.
-  we have a logo already made and has registered in Uganda. our logo colors are mixture between a lot of brown color and yellow. vacuum  plastic bags.
- there is no restrictions towards your imagination .
-  all details available
- we will launch our product through phases ;
- phase 1 is  a ground coffee : ( Turkish coffee )  2 degrees of roasting which are ( medium dark , light ) of 250 grm
b) roasted beans: 2 degrees ( medium, dark) of 250 grm & 1000 grm
- we need also to highlight the eastern spirit of Turkish coffee
- we  need designs, the info and color only will be changed depending on previous classifications

Target Market(s)
Arab countries, Turkey , Uganda, Europe
Colors
Designer to choose colors to be used in the design.
Requirements
Nice to have
- about nature , Elgon mountain , farmers, freshness, distinctive product, soul of east such as decorated cup of Turkish coffee . these just an ideas but there is no restrictions on your imagination

```html
<!DOCTYPE html>
<html lang="en">
<head>
<meta charset="utf-8">
<title>Velmoraq Arabica – 250 g pack</title>
<link href="https://fonts.googleapis.com/css2?family=Titan+One&family=Quicksand:wght@600;700&family=PT+Sans+Narrow:wght@400;700&display=swap" rel="stylesheet">
<style>
  :root{
    --brown:#4e2d10;
    --brown-deep:#3a1f08;
    --seam:#7b5a31;
    --tan:#c4a06a;
    --tan-light:#d8bc8a;
    --cream:#f1e6d0;
    --white:#ffffff;
    --band:#a6804c;
  }
  *{margin:0;padding:0;box-sizing:border-box}
  html,body{width:1080px;height:1200px;overflow:hidden;background:var(--white)}
  .canvas{position:relative;width:1080px;height:1200px;overflow:hidden;background:var(--white)}
  .stage{position:absolute;left:0;top:0;width:1024px;height:1130px;transform:scale(1.0547,1.0619);transform-origin:0 0}
  .pack{position:absolute;left:42px;top:37px;width:938px;height:1063px;background:var(--brown);border:1px solid var(--seam)}
  .fold{position:absolute;top:37px;width:1px;height:1063px;background:var(--seam)}
  .band{position:absolute;left:42px;width:938px}
  .band--top{top:170px;height:22px;background:linear-gradient(var(--band),var(--tan) 50%,var(--band))}
  .band--thin{height:24px;background:linear-gradient(var(--band),var(--tan) 50%,var(--band))}
  .band--wide{top:1000px;height:55px;background:linear-gradient(var(--brown-deep),#6b4a28 50%,var(--brown-deep))}
  .panel{position:absolute;top:37px;height:1063px;text-align:center}
  .panel--left{left:42px;width:256px}
  .panel--center{left:298px;width:425px}
  .panel--right{left:723px;width:257px}
  .panel>*{position:absolute;left:0;right:0}
  .brand{font-family:"Quicksand",sans-serif;font-weight:700;color:var(--cream);display:flex;justify-content:center;align-items:center}
  .brand span{background:var(--brown);padding:4px 12px;border-radius:4px}
  .brand--side{top:130px;font-size:22px}
  .brand--main{top:125px;font-size:34px}
  .title{font-family:"Titan One",sans-serif;color:var(--white);letter-spacing:1px;
    text-shadow:-2px -2px 0 var(--brown-deep),2px -2px 0 var(--brown-deep),-2px 2px 0 var(--brown-deep),2px 2px 0 var(--brown-deep),3px 4px 0 var(--tan-light)}
  .title--side{top:258px;font-size:37px}
  .title--main{top:660px;font-size:66px}
  .subtitle{font-family:"Quicksand",sans-serif;font-weight:700;color:var(--cream)}
  .subtitle--side{top:306px;font-size:15px}
  .subtitle--main{top:733px;font-size:26px;color:var(--tan)}
  .origin{font-family:"Quicksand",sans-serif;font-weight:700;color:var(--cream)}
  .origin--side{top:330px;font-size:15px}
  .origin--main{top:775px;font-size:25px;color:var(--white)}
  .estate{top:371px;font-family:"PT Sans Narrow",sans-serif;font-weight:700;font-size:20px;color:var(--cream)}
  .copy{font-family:"PT Sans Narrow",sans-serif;font-size:15px;line-height:21.6px;color:var(--cream);margin:0 auto;width:205px}
  .copy--bold{font-weight:700}
  .weight{top:875px;font-family:"Quicksand",sans-serif;font-weight:700;font-size:34px;color:var(--tan)}
  .artwork{position:absolute;left:350px;top:345px;width:315px;height:265px;border-radius:50%;
    background:radial-gradient(ellipse at center,rgba(196,160,106,.75) 0%,rgba(196,160,106,.35) 55%,rgba(196,160,106,0) 72%)}
  .roast{top:810px;display:flex;justify-content:center;align-items:center;gap:14px}
  .roast__label{font-family:"Quicksand",sans-serif;font-weight:700;font-size:15px;line-height:15px;color:var(--tan);text-align:left}
</style>
</head>
<body>
<div class="canvas">
  <div class="stage">
    <div class="pack"></div>
    <div class="band band--top" role="img" aria-label="Decorative ornament border"></div>
    <div class="band band--thin" style="top:976px" role="img" aria-label="Decorative ornament border"></div>
    <div class="band band--wide" role="img" aria-label="Wide decorative tribal pattern band"></div>
    <div class="band band--thin" style="top:1055px" role="img" aria-label="Decorative ornament border"></div>
    <div class="fold" style="left:298px"></div>
    <div class="fold" style="left:723px"></div>

    <section class="panel panel--left">
      <div class="brand brand--side"><span>Velmoraq</span></div>
      <h2 class="title title--side">ARABICA</h2>
      <p class="subtitle subtitle--side">roasted coffee beans</p>
      <p class="origin origin--side">UGANDA</p>
      <h3 class="estate">Tesmo Kirul</h3>
      <p class="copy copy--bold" style="top:398px">Specialty Arabica coffee grown at slopes of Mountain Elgon with rich volcanic soils located in Eastern region of Uganda.</p>
      <p class="copy" style="top:575px">Specialty Arabica coffee grown at slopes of Mountain Elgon with rich volcanic soils located in Eastern region of Uganda. Specialty Arabica coffee grown slopes of Mountain Elgon with rich volcanic soils located in Eastern region specialty Arabica coffee grown at slopes of Mountain Elgon with rich volcanic soils located in Eastern region of Uganda.</p>
      <p class="weight">250 g</p>
    </section>

    <section class="panel panel--center">
      <div class="brand brand--main"><span>Velmoraq</span></div>
      <h1 class="title title--main">ARABICA</h1>
      <p class="subtitle subtitle--main">roasted coffee beans</p>
      <p class="origin origin--main">UGANDA</p>
      <p class="weight">250 g</p>
    </section>
    <div class="artwork" role="img" aria-label="Illustration of coffee leaves above Mount Elgon with trees, a cup of coffee and scattered coffee beans"></div>

    <section class="panel panel--right">
      <div class="brand brand--side"><span>Velmoraq</span></div>
      <h2 class="title title--side">ARABICA</h2>
      <p class="subtitle subtitle--side">roasted coffee beans</p>
      <p class="origin origin--side">UGANDA</p>
      <p class="copy" style="top:372px">Specialty Arabica coffee grown at slopes of Mountain Elgon with rich volcanic soils located in Eastern region of Uganda. Specialty Arabica coffee grown slopes of Mountain Elgon with rich volcanic soils located in Eastern region specialty Arabica coffee grown at slopes of Mountain Elgon with rich volcanic soils located in Eastern region of Uganda.</p>
      <p class="copy copy--bold" style="top:673px">Specialty Arabica coffee grown at slopes of Mountain Elgon with rich volcanic soils located in Eastern region of Uganda.</p>
      <div class="roast">
        <p class="roast__label">Roasting<br>degrees</p>
        <svg width="96" height="30" viewBox="0 0 96 30" aria-label="Roast level 3 of 5">
          <g stroke="var(--tan)" stroke-width="1.5">
            <ellipse cx="9" cy="15" rx="7" ry="12" fill="var(--tan)"/>
            <ellipse cx="28" cy="15" rx="7" ry="12" fill="var(--tan)"/>
            <ellipse cx="47" cy="15" rx="7" ry="12" fill="var(--tan)"/>
            <ellipse cx="66" cy="15" rx="7" ry="12" fill="none"/>
            <ellipse cx="85" cy="15" rx="7" ry="12" fill="none"/>
          </g>
          <g stroke="var(--brown)" stroke-width="1.2" fill="none">
            <path d="M9 4 Q6 15 9 26"/><path d="M28 4 Q25 15 28 26"/><path d="M47 4 Q44 15 47 26"/>
          </g>
          <g stroke="var(--tan)" stroke-width="1.2" fill="none">
            <path d="M66 4 Q63 15 66 26"/><path d="M85 4 Q82 15 85 26"/>
          </g>
        </svg>
      </div>
      <p class="weight">250 g</p>
    </section>
  </div>
</div>
</body>
</html>
```